依頼概要
■依頼の目的/概要
弊社ではあささんぽ、ひなたを浴びようと思えるSNSアプリの制作を行っております。
ほしぞらノートアプリでは毎日の記録をつけるためのライフログ系の機能を制作しております。

ライフログとして自分の記録を見返したり、他のユーザーからも見てもらえる機能がある日記のデザイン及びその画面のUI制作をお願いします。

■依頼の詳細
ユーザーが投稿するのは朝日を含めた毎朝の日記で自分のほしぞらノート(本のテイスト)の左ページを投稿します(アプリ上ホーム画面)。その日記投稿や朝散歩をすればするほど幸せの証として「きらりリボン」を報酬として獲得し、毎朝獲得したハートを自分のほしぞらノートの右ページに貯めておけます(アプリ上ほしぞらノート画面)。

今回トライアルでお願いしたいのはユーザーが朝日を投稿するホーム画面のUIです(左ページ)。
必要な要項といたしましては、
・ユーザーが撮影した朝日の写真(必須)
・日付(必須)
・天気※
・場所※
・気温※
・日記コメント※
・自分のキャラクター(こちらは素材があります)※

を入れられるようにしたいと考えております。
※は、ユーザー任意で入れたり、非表示にできます

スワイプすると、他のユーザーの日記のページをめくるような感覚のモーションの検討もしています。

こちらをトライアルという形で、採用された方には別画面/別バージョンの本のデザインや詳細なUIなどご相談したいと考えております。追加のUIのお見積りなども含め、ご提案いただけますと幸いです。

現在の開発中の仮デザインを添付しますが、よりよいデザインを是非、応募いただけますと幸いです。

画面UIのデザインがイメージと合っていた為。

この度、ご提案いただきありがとうございました。ご厚情にお応えすることができず、誠に申し訳ございません。勝手ではございますが、これに懲りず今後ともお付き合いくださいますようお願い申し上げます。

```html
<!DOCTYPE html>
<html lang="ja">
<head>
<meta charset="UTF-8">
<title>ほしぞらノート ホーム</title>
<link rel="stylesheet" href="https://fonts.googleapis.com/css2?family=Noto+Sans+JP:wght@400;500;700&display=swap">
<style>
:root{
  --wood:#e6c58a;
  --wood-dark:#d9b273;
  --cover:#9c2f4b;
  --cover-dark:#7d2239;
  --page:#fcf4cc;
  --page-edge:#efe2a8;
  --navy:#1e3857;
  --white:#ffffff;
  --pink:#e9467a;
  --orange:#f39a1c;
  --green:#8cc63f;
  --violet:#6b6fe0;
  --heart:#ef5a78;
}
*{margin:0;padding:0;box-sizing:border-box}
html,body{width:1200px;height:2400px;overflow:hidden}
body{
  position:relative;
  font-family:"Noto Sans JP",sans-serif;
  color:var(--navy);
  background:linear-gradient(180deg,var(--wood) 0%,var(--wood-dark) 100%);
}
.top-bar{position:absolute;left:44px;right:44px;top:46px;display:flex;justify-content:space-between;color:var(--white);font-size:36px;font-weight:500}
.top-bar .diary-title{text-decoration:underline;text-underline-offset:6px}
.book-cover{position:absolute;left:20px;top:116px;width:1160px;height:2256px;background:var(--cover);border-radius:24px;box-shadow:0 8px 0 var(--cover-dark)}
.page-stack{position:absolute;left:76px;top:140px;width:1092px;height:2188px;background:var(--page-edge);border-radius:0 24px 40px 0}
.page{position:absolute;left:84px;top:148px;width:1076px;height:2150px;background:var(--page);border-radius:16px 24px 60px 16px;box-shadow:0 6px 10px rgba(0,0,0,.12)}
.tab{position:absolute;left:20px;width:96px;height:168px;border-radius:20px 0 0 20px;display:flex;align-items:center;justify-content:center}
.tab svg{width:52px;height:52px}
.tab-home{top:320px;background:var(--pink)}
.tab-menu{top:500px;background:var(--orange)}
.tab-clip{top:688px;background:var(--green)}
.tab-help{top:872px;background:var(--violet)}
.circle-btn{position:absolute;width:88px;height:88px;border-radius:50%;background:var(--navy);display:flex;align-items:center;justify-content:center}
.circle-btn svg{width:44px;height:44px}
.nav-prev{left:176px;top:220px}
.nav-next{left:284px;top:220px}
.new-post{position:absolute;left:808px;top:220px;width:320px;height:92px;border-radius:46px;background:var(--navy);color:var(--white);font-size:38px;font-weight:500;display:flex;align-items:center;gap:22px;padding-left:30px}
.new-post .plus{width:46px;height:46px;border-radius:50%;background:var(--white);display:flex;align-items:center;justify-content:center}
.photo-frame{position:absolute;left:332px;top:392px;width:620px;height:620px;background:var(--white);box-shadow:0 10px 22px rgba(0,0,0,.22)}
.photo{position:absolute;left:24px;top:20px;width:572px;height:572px;background:linear-gradient(180deg,#f3d9a6 0%,#a9a6a0 45%,#4a4a4c 100%)}
.zoom{position:absolute;left:818px;top:880px;width:88px;height:88px;border-radius:50%;background:rgba(30,30,30,.85);display:flex;align-items:center;justify-content:center}
.zoom svg{width:50px;height:50px}
.meta{position:absolute;left:186px;top:1096px;font-size:38px;line-height:56px;font-weight:500}
.headline{position:absolute;left:186px;top:1290px;font-size:58px;font-weight:700}
.body-text{position:absolute;left:186px;top:1400px;width:940px;font-size:43px;line-height:81px;font-weight:500;text-align:justify;height:324px;overflow:hidden}
.edit-btn{position:absolute;left:186px;top:1808px;width:216px;height:88px;border-radius:44px;background:var(--navy);color:var(--white);font-size:38px;font-weight:500;display:flex;align-items:center;justify-content:center;gap:16px}
.edit-btn svg{width:44px;height:44px}
.tag-btn{left:428px;top:1808px}
.trash-btn{left:540px;top:1808px}
.heart-btn{position:absolute;left:1036px;top:1808px;width:88px;height:88px;border-radius:50%;background:var(--heart);display:flex;align-items:center;justify-content:center}
.heart-btn svg{width:46px;height:46px}
.divider{position:absolute;left:186px;top:1958px;width:940px;height:5px;background:var(--navy)}
.avatar{position:absolute;left:186px;top:2000px;width:176px;height:176px;border-radius:50%;background:linear-gradient(180deg,#fff6d8 0%,#f5d66b 100%);border:6px solid var(--white);box-shadow:0 0 0 3px #e6dcb0}
.profile{position:absolute;left:410px;top:2010px;font-size:40px;line-height:64px;font-weight:500}
.profile .link{text-decoration:underline;text-underline-offset:6px}
</style>
</head>
<body>
<header class="top-bar"><span class="diary-title">日記のタイトル / 現在のページ名</span><span class="page-count">000 / 000</span></header>

<div class="book-cover"></div>
<div class="page-stack"></div>
<main class="page"></main>

<nav>
  <div class="tab tab-home"><svg viewBox="0 0 24 24"><path d="M3 11 12 3l9 8v10h-6v-6H9v6H3z" fill="#fff"/></svg></div>
  <div class="tab tab-menu"><svg viewBox="0 0 24 24"><path d="M4 6h16M4 12h16M4 18h16" stroke="#fff" stroke-width="3" stroke-linecap="round"/></svg></div>
  <div class="tab tab-clip"><svg viewBox="0 0 24 24"><path d="M16 7v9a4 4 0 0 1-8 0V6a2.5 2.5 0 0 1 5 0v9a1 1 0 0 1-2 0V8" fill="none" stroke="#fff" stroke-width="2.2" stroke-linecap="round"/></svg></div>
  <div class="tab tab-help"><svg viewBox="0 0 24 24"><circle cx="12" cy="12" r="10" fill="#fff"/><path d="M9.5 9.5a2.5 2.5 0 1 1 3.5 2.3c-.7.3-1 .8-1 1.5v.7" fill="none" stroke="#6b6fe0" stroke-width="2.2" stroke-linecap="round"/><circle cx="12" cy="17.3" r="1.3" fill="#6b6fe0"/></svg></div>
</nav>

<div class="circle-btn nav-prev"><svg viewBox="0 0 24 24"><path d="M15 5l-7 7 7 7" fill="none" stroke="#fff" stroke-width="3" stroke-linecap="round" stroke-linejoin="round"/></svg></div>
<div class="circle-btn nav-next"><svg viewBox="0 0 24 24"><path d="M9 5l7 7-7 7" fill="none" stroke="#fff" stroke-width="3" stroke-linecap="round" stroke-linejoin="round"/></svg></div>
<div class="new-post"><span class="plus"><svg viewBox="0 0 24 24" width="30" height="30"><path d="M12 5v14M5 12h14" stroke="#1e3857" stroke-width="3.5" stroke-linecap="round"/></svg></span>新規投稿</div>

<figure class="photo-frame"><div class="photo" role="img" aria-label="朝日の中を散歩する犬の写真"></div></figure>
<div class="zoom"><svg viewBox="0 0 24 24"><circle cx="10" cy="10" r="6" fill="none" stroke="#fff" stroke-width="2.4"/><path d="M14.5 14.5 20 20M10 7v6M7 10h6" stroke="#fff" stroke-width="2.4" stroke-linecap="round"/></svg></div>

<section class="meta">
  <p>投稿日／ 2023 年 00 月 00 日</p>
  <p>天気／晴れ</p>
  <p>気温／ 00 度</p>
</section>
<h1 class="headline">見出しタイトルテキスト</h1>
<p class="body-text">吾輩は猫である。名前はまだ無い。どこで生れたかとんと見当がつかぬ。何でも薄暗いじめじめした所でニャーニャー泣いていた事だけは記憶している。吾輩はここで始めて人間というものを見た。しかも</p>

<div class="edit-btn"><svg viewBox="0 0 24 24"><path d="M4 20v-3.5L15 5.5l3.5 3.5L7.5 20zM16.5 4l1.5-1.5 3.5 3.5L20 7.5z" fill="#fff"/></svg>編集</div>
<div class="circle-btn tag-btn"><svg viewBox="0 0 24 24"><path d="M3 12V4a1 1 0 0 1 1-1h8l9 9-9 9z" fill="#fff"/><circle cx="7.5" cy="7.5" r="1.6" fill="#1e3857"/></svg></div>
<div class="circle-btn trash-btn"><svg viewBox="0 0 24 24"><path d="M5 6h14M9 6V4h6v2M6.5 6l1 14h9l1-14" fill="none" stroke="#fff" stroke-width="2.2" stroke-linejoin="round"/><path d="M10 10v7M14 10v7" stroke="#fff" stroke-width="2"/></svg></div>
<div class="heart-btn"><svg viewBox="0 0 24 24"><path d="M12 21s-8-5.2-8-11a4.5 4.5 0 0 1 8-2.8A4.5 4.5 0 0 1 20 10c0 5.8-8 11-8 11z" fill="#fff"/></svg></div>

<div class="divider"></div>
<div class="avatar" role="img" aria-label="投稿者のキャラクターイラスト"></div>
<section class="profile">
  <p>【投稿者】<span class="link">ひなた</span></p>
  <p>【SNS】<span class="link">Pipit</span> / <span class="link">Nakama</span> / <span class="link">Photoly</span></p>
  <p>【ハートの数】0,000</p>
</section>
</body>
</html>
```